prestige web design for VELTA Finance

Hi Guys,

Looking to team up with a creative designer for another of our websites for VELTA finance.
if looking for our similar website www.brimlowfinance.com.au is one of our other companies. ideally working in our logo being black and white.

Please see attachments for our logo and a description
HOME
VEHICLE
EQUIPMENT
WHO WE ARE
CONTACT US

open to ideas on layout .

touch base if you have any questions.

Target Market(s)

Prestige cars and equipment -trucks earthmoving

Industry/Entity Type

finance

Coding

Coded - Design and coding required

Number of Pages Required

5+ page

Font styles to use
Sans Serif

Colors

Designer to choose colors to be used in the design.

```html
<!DOCTYPE html>
<html lang="en">
<head>
<meta charset="utf-8">
<title>VELTA Finance</title>
<link href="https://fonts.googleapis.com/css2?family=Oswald:wght@300;400;700&family=Roboto:ital,wght@0,400;0,500;0,700;1,500&display=swap" rel="stylesheet">
<style>
:root{
  --ink:#161616;
  --dark:#1b1b1b;
  --white:#ffffff;
  --grey-bg:#f1f2f4;
  --text:#5c5c5c;
  --muted:#8a8a8a;
  --line:#d9d9d9;
}
*{box-sizing:border-box;margin:0;padding:0}
html,body{width:1200px;height:4412px;overflow:hidden}
body{font-family:"Roboto",Arial,sans-serif;color:var(--text);background:var(--white);position:relative}
.abs{position:absolute}
.heading{font-family:"Oswald","Arial Narrow",sans-serif;font-weight:300;text-transform:uppercase;color:var(--ink);font-size:37px;letter-spacing:.5px;line-height:1}
.heading b{font-weight:700}
.heading.light{color:var(--white)}
.btn{position:absolute;display:flex;align-items:center;justify-content:center;border-radius:23px;font-weight:700;font-size:14px;text-transform:uppercase;letter-spacing:.3px}
.btn.white{background:var(--white);color:var(--ink)}
.btn.black{background:var(--ink);color:var(--white)}

/* hero */
.hero{left:0;top:0;width:1200px;height:1150px;background:var(--dark);overflow:hidden}
.hero-photo{left:0;top:0;width:1200px;height:712px;background:linear-gradient(100deg,#5a3a34 0%,#8d8d8f 30%,#b9bcc2 55%,#9ea3aa 80%,#d7d9dc 100%)}
.hero-shade{left:0;top:0;width:1200px;height:712px;background:linear-gradient(180deg,rgba(0,0,0,.35),rgba(0,0,0,.1) 40%,rgba(0,0,0,.25))}
.nav-logo{left:111px;top:24px;color:var(--white);font-weight:500;font-size:34px;letter-spacing:1px}
.nav{left:442px;top:33px;display:flex;gap:32px}
.nav a{color:var(--white);font-size:12px;font-style:italic;font-weight:500;text-decoration:none;text-transform:uppercase}
.nav a.active{border-bottom:1px solid var(--white);padding-bottom:6px}
.nav-call{left:938px;top:21px;display:flex;align-items:center;gap:22px;color:var(--white);font-size:13px;font-style:italic;font-weight:500}
.circle-icon{width:40px;height:40px;border-radius:50%;background:var(--white);display:flex;align-items:center;justify-content:center}
.hero-title{left:0;width:1200px;top:272px;text-align:center;color:var(--white);font-family:"Oswald",sans-serif;font-weight:400;font-size:37px;text-transform:uppercase}
.hero-sub{left:0;width:1200px;top:328px;text-align:center;color:var(--white);font-size:16px;line-height:27px}
.arrow{width:38px;height:38px;border-radius:50%;background:var(--white);top:279px;display:flex;align-items:center;justify-content:center}
.mouse{left:587px;top:590px;width:26px;height:54px;border:2px solid var(--white);border-radius:14px}

/* calculator */
.calc-title{left:0;width:1200px;top:770px;text-align:center}
.rule{height:2px;background:var(--white)}
.calc-label{color:var(--white);font-size:14px}
.field{height:44px;border:1px solid rgba(255,255,255,.85);border-radius:22px;color:var(--white);font-size:14px;padding:0 14px;display:flex;align-items:center;justify-content:space-between}

/* about */
.photo{border-radius:0}
.card{background:var(--white);box-shadow:0 6px 26px rgba(0,0,0,.12)}
.body-text{font-size:13.5px;line-height:25.7px;color:var(--text);text-align:justify}
.body-text strong{color:var(--ink)}

/* why */
.why{left:0;top:1777px;width:1200px;height:748px;background:var(--grey-bg)}
.service-title{font-size:17px;font-weight:700;color:var(--ink);text-transform:uppercase}
.apply{font-size:12px;font-weight:700;color:var(--ink);text-transform:uppercase;display:flex;align-items:center;gap:7px}
.icon-box{width:86px;height:86px;background:#eeeeef;display:flex;align-items:center;justify-content:center}

/* who */
.who{left:0;top:2525px;width:1200px;height:442px;background:linear-gradient(120deg,#2c2f35,#3a3d43 45%,#25272b)}
.who-shade{left:0;top:0;width:1200px;height:442px;background:rgba(20,22,26,.55)}

/* serve */
.serve-list{list-style:none}
.serve-list li{position:relative;padding-left:32px;font-size:13.5px;line-height:22.5px;margin-bottom:11px;color:var(--muted)}
.serve-list li b{font-weight:400;color:var(--ink)}
.serve-list li::before{content:"";position:absolute;left:0;top:5px;width:12px;height:12px;border-radius:50%;background:var(--ink)}

/* contact */
.contact{left:0;top:3588px;width:1200px;height:522px;background:linear-gradient(180deg,#eef0f3,#e5e7ea)}
.input{background:var(--white);border-radius:22px;height:44px;font-size:13px;color:var(--muted);padding:0 22px;display:flex;align-items:center}

/* footer */
.footer{left:0;top:4110px;width:1200px;height:302px;background:var(--ink);color:var(--white)}
.foot-nav{display:flex;justify-content:center;gap:22px;font-size:15px;font-style:italic;font-weight:500;text-transform:uppercase;color:var(--white)}
.foot-nav span.sep{font-weight:400}
.social{width:32px;height:32px;border-radius:50%;background:#444}
.social.first{background:var(--white)}
</style>
</head>
<body>

<!-- HERO + CALCULATOR -->
<section class="abs hero">
  <div class="abs hero-photo" role="img" aria-label="Couple buying a car from a salesman in a bright car showroom"></div>
  <div class="abs hero-shade"></div>
  <svg class="abs" style="left:0;top:0" width="1200" height="1150" viewBox="0 0 1200 1150">
    <polygon points="0,520 600,712 1200,513 1200,1150 0,1150" fill="#1b1b1b"/>
    <polyline points="0,520 600,712 1200,513" fill="none" stroke="#ffffff" stroke-width="9"/>
  </svg>

  <div class="abs nav-logo">VELTA Finance</div>
  <nav class="abs nav">
    <a class="active">Home</a><a>Vehicle</a><a>Equipment</a><a>Who We Are</a><a>Contact Us</a>
  </nav>
  <div class="abs nav-call">
    <div class="circle-icon"><svg width="16" height="16" viewBox="0 0 24 24"><path fill="#161616" d="M6.6 10.8a15.1 15.1 0 0 0 6.6 6.6l2.2-2.2c.3-.3.7-.4 1-.2 1.1.4 2.3.6 3.6.6.6 0 1 .4 1 1V20c0 .6-.4 1-1 1A17 17 0 0 1 3 4c0-.6.4-1 1-1h3.5c.6 0 1 .4 1 1 0 1.3.2 2.5.6 3.6.1.3 0 .7-.2 1z"/></svg></div>
    <span>CALL 13 48 27</span>
  </div>

  <div class="abs arrow" style="left:34px"><svg width="14" height="14" viewBox="0 0 14 14"><path d="M9 2 4 7l5 5" fill="none" stroke="#161616" stroke-width="2.4"/></svg></div>
  <div class="abs arrow" style="left:1126px"><svg width="14" height="14" viewBox="0 0 14 14"><path d="M5 2l5 5-5 5" fill="none" stroke="#161616" stroke-width="2.4"/></svg></div>

  <h1 class="abs hero-title">Welcome to VELTA Finance</h1>
  <p class="abs hero-sub">We are committed to providing individuals &amp; businesses<br>with tailored financial services</p>
  <div class="btn white" style="left:523px;top:404px;width:154px;height:45px">Get Started</div>

  <div class="abs mouse">
    <div class="abs" style="left:9px;top:10px;width:5px;height:5px;border-radius:50%;background:#fff"></div>
    <svg class="abs" style="left:6px;top:28px" width="11" height="8" viewBox="0 0 11 8"><path d="M1 1l4.5 4.5L10 1" fill="none" stroke="#fff" stroke-width="1.6"/></svg>
  </div>

  <h2 class="abs heading light calc-title">Finance Repayment <b>Calculator</b></h2>
  <div class="abs rule" style="left:553px;top:814px;width:94px"></div>

  <div class="abs calc-label" style="left:146px;top:852px">Purchase amount:</div>
  <div class="abs calc-label" style="left:454px;top:852px">Deposit:</div>
  <div class="abs calc-label" style="left:760px;top:852px">Term: &#9432;</div>
  <div class="abs field" style="left:146px;top:882px;width:292px">$</div>
  <div class="abs field" style="left:454px;top:882px;width:292px">$</div>
  <div class="abs field" style="left:760px;top:882px;width:292px"><span>3 years</span><svg width="10" height="7" viewBox="0 0 10 7"><path d="M1 1l4 4 4-4" fill="none" stroke="#fff" stroke-width="1.5"/></svg></div>

  <div class="abs calc-label" style="left:146px;top:948px">Interest rate % p.a: &#9432;</div>
  <div class="abs calc-label" style="left:454px;top:948px">Balloon payment: &#9432;</div>
  <div class="abs calc-label" style="left:760px;top:948px">Monthly: &#9432;</div>
  <div class="abs field" style="left:146px;top:978px;width:292px">7.5</div>
  <div class="abs field" style="left:454px;top:978px;width:292px">$</div>
  <div class="abs field" style="left:760px;top:978px;width:292px"></div>

  <div class="btn white" style="left:523px;top:1041px;width:154px;height:46px">Calculate</div>
</section>

<!-- ABOUT -->
<section>
  <div class="abs photo" style="left:550px;top:1246px;width:539px;height:428px;background:linear-gradient(110deg,#6a6e74,#a9adb3 50%,#54585e)" role="img" aria-label="Adviser shaking hands with a couple across an office desk"></div>
  <div class="abs" style="left:609px;top:1270px;width:4px;height:372px;background:#fff"></div>
  <div class="abs card" style="left:111px;top:1277px;width:488px;height:363px;padding:30px 25px 0 25px">
    <div style="display:flex;align-items:center;gap:16px">
      <h2 class="heading">About <b>VELTA</b></h2>
      <div style="width:56px;height:3px;background:var(--ink)"></div>
    </div>
    <p class="body-text" style="margin-top:28px"><strong>VELTA Finance</strong> has nearly 20 years industry experience, so we certainly understand personal and business lending. We are committed to providing individuals and businesses with tailored financial services that enable them to reach and then exceed their financial goals.</p>
    <p class="body-text" style="margin-top:11px">We have a vast list of lenders to suit along with an online team ready to help you, so we're easily accessible and here when you need us. Our friendly team of experienced and approachable staff that will listen, understand your situation and lend responsibly.</p>
  </div>
</section>

<!-- WHY CHOOSE US -->
<section class="abs why">
  <h2 class="abs heading" style="left:0;width:1200px;top:63px;text-align:center">Why <b>Choose Us?</b></h2>
  <p class="abs" style="left:200px;width:800px;top:136px;text-align:center;font-size:15px;line-height:27px">Well, because we&amp;#39;re here to help you! We care about outcomes AND helping you achieve a stress and enjoyable lending experience.</p>

  <div class="abs photo" style="left:111px;top:221px;width:476px;height:341px;background:linear-gradient(120deg,#5b4a40,#a69b92 50%,#3f444c)" role="img" aria-label="Customer receiving car keys at a dealership desk"></div>
  <div class="abs card" style="left:135px;top:529px;width:428px;height:159px">
    <div class="abs icon-box" style="left:16px;top:33px"><svg width="52" height="52" viewBox="0 0 52 52" fill="none" stroke="#161616" stroke-width="2"><circle cx="26" cy="12" r="8"/><path d="M8 36l4-10h28l4 10v8H8z"/><circle cx="16" cy="38" r="3"/><circle cx="36" cy="38" r="3"/></svg></div>
    <div class="abs service-title" style="left:121px;top:24px">Vehicle Loan</div>
    <p class="abs" style="left:121px;top:58px;width:290px;font-size:12.5px;line-height:22px">While you focus on getting the right car, we will focus on getting you the right finance.</p>
    <div class="abs apply" style="left:121px;top:116px">Apply Now <svg width="12" height="12" viewBox="0 0 12 12"><circle cx="6" cy="6" r="6" fill="#161616"/><path d="M5 3.5 7.5 6 5 8.5" stroke="#fff" stroke-width="1.5" fill="none"/></svg></div>
  </div>

  <div class="abs photo" style="left:611px;top:221px;width:478px;height:341px;background:linear-gradient(120deg,#7b6f66,#c9c3bd 50%,#6f7378)" role="img" aria-label="Business team working at a laptop in an office"></div>
  <div class="abs card" style="left:636px;top:529px;width:428px;height:159px">
    <div class="abs icon-box" style="left:16px;top:33px"><svg width="52" height="52" viewBox="0 0 52 52" fill="none" stroke="#161616" stroke-width="2"><circle cx="18" cy="14" r="6"/><circle cx="34" cy="20" r="7"/><path d="M6 40h14l10-6h10M6 34h12"/></svg></div>
    <div class="abs service-title" style="left:121px;top:24px">Equipment</div>
    <p class="abs" style="left:121px;top:58px;width:290px;font-size:12.5px;line-height:22px;text-align:justify">At VELTA, we help businesses of all sizes to secure funding in the form of a business loan</p>
    <div class="abs apply" style="left:121px;top:116px">Apply Now <svg width="12" height="12" viewBox="0 0 12 12"><circle cx="6" cy="6" r="6" fill="#161616"/><path d="M5 3.5 7.5 6 5 8.5" stroke="#fff" stroke-width="1.5" fill="none"/></svg></div>
  </div>
</section>

<!-- WHO WE ARE -->
<section class="abs who" role="img" aria-label="Dark toned photo of people signing documents">
  <div class="abs who-shade"></div>
  <h2 class="abs heading light" style="left:0;width:1200px;top:73px;text-align:center">Who <b>We Are</b></h2>
  <p class="abs" style="left:128px;width:944px;top:152px;text-align:center;color:#fff;font-size:14px;line-height:26.7px">The goal of VELTA Finance is to build on the track record of the VELTA business and to create a new benchmark in the Australia's Asset Finance industry, providing good old fashioned localised service that delivers the assets you want when you need them and structured to recognise asset useful life while being sensitive to cashflow. providing second to none asset finance support to business owners and individuals alike. A healthy appetite exists to help our customers with finance for a broad range of motor vehicles (from cars to heavy commercial vehicles), mobile and fixed plant, and business equipment...for more detail you can contact us today.</p>
  <div class="btn white" style="left:527px;top:322px;width:146px;height:46px">Read More</div>
</section>

<!-- WHAT WE SERVE -->
<section>
  <div class="abs photo" style="left:111px;top:3056px;width:539px;height:426px;background:linear-gradient(120deg,#8a6d52,#cfc4b8 45%,#5d5f63)" role="img" aria-label="Smiling couple holding new keys at a table"></div>
  <div class="abs" style="left:592px;top:3080px;width:4px;height:378px;background:#fff"></div>
  <div class="abs card" style="left:587px;top:3087px;width:502px;height:364px;padding:30px 30px 0 42px">
    <div style="display:flex;align-items:center;gap:16px">
      <h2 class="heading">What <b>We Searve</b></h2>
      <div style="width:56px;height:3px;background:var(--ink)"></div>
    </div>
    <ul class="serve-list" style="margin-top:26px;text-align:justify">
      <li><b>Transport &amp; Logistics:</b> Trucks, vans, trailers, ships, forklifts, conveyors, conveyance robots etc.</li>
      <li><b>Construction, Earthmoving, Forestry and Farming:</b> Scaffolding tower, digger, shovel loggers, harvesters etc.</li>
      <li><b>Healthcare:</b> dental machinery, medical imaging machines, Veterinary equipment etc.</li>
      <li><b>Automotive:</b> Cars, utes, motorbikes etc.</li>
      <li><b>Technology:</b> computers, laptops, printers/copiers, servers, upgrading to new system software, etc.</li>
    </ul>
  </div>
</section>

<!-- CONTACT -->
<section class="abs contact" role="img" aria-label="Faded photo of a desk with a small house model and laptop">
  <h2 class="abs heading" style="left:0;width:1200px;top:47px;text-align:center">Contact <b>Us</b></h2>
  <div class="abs rule" style="left:553px;top:92px;width:94px;background:var(--ink)"></div>
  <div class="abs" style="left:362px;top:123px;display:flex;align-items:center;gap:18px;font-size:13px;color:var(--ink)">
    <div class="circle-icon" style="background:var(--ink)"><svg width="16" height="16" viewBox="0 0 24 24"><path fill="#fff" d="M6.6 10.8a15.1 15.1 0 0 0 6.6 6.6l2.2-2.2c.3-.3.7-.4 1-.2 1.1.4 2.3.6 3.6.6.6 0 1 .4 1 1V20c0 .6-.4 1-1 1A17 17 0 0 1 3 4c0-.6.4-1 1-1h3.5c.6 0 1 .4 1 1 0 1.3.2 2.5.6 3.6.1.3 0 .7-.2 1z"/></svg></div>
    <span><b>CALL US:</b> 13 48 27</span>
    <div class="circle-icon" style="background:var(--ink);margin-left:10px"><svg width="16" height="14" viewBox="0 0 16 14"><rect x="1" y="2" width="14" height="10" fill="#fff"/><path d="M1 2l7 5 7-5" stroke="#161616" stroke-width="1.4" fill="none"/></svg></div>
    <span><b>EMAIL US:</b> info@veltafinance.com</span>
  </div>
  <div class="abs input" style="left:146px;top:195px;width:292px">First Name</div>
  <div class="abs input" style="left:454px;top:195px;width:292px">Last Name</div>
  <div class="abs input" style="left:760px;top:195px;width:292px">Phone Number</div>
  <div class="abs input" style="left:146px;top:256px;width:292px">Regional Location</div>
  <div class="abs input" style="left:454px;top:256px;width:292px">Email Address</div>
  <div class="abs input" style="left:760px;top:256px;width:292px">Subject</div>
  <div class="abs input" style="left:146px;top:317px;width:906px;height:92px;align-items:flex-start;padding-top:14px;border-radius:46px">Message</div>
  <div class="btn black" style="left:515px;top:425px;width:170px;height:46px">Send Message</div>
</section>

<!-- FOOTER -->
<footer class="abs footer">
  <div class="abs" style="left:0;width:1200px;top:46px;text-align:center;font-size:34px;font-weight:500;letter-spacing:1px">VELTA Finance</div>
  <div class="abs foot-nav" style="left:0;width:1200px;top:114px">
    <span>Home</span><span class="sep">/</span><span>Vehicle</span><span class="sep">/</span><span>Equipment</span><span class="sep">/</span><span>Who We Are</span><span class="sep">/</span><span>Contact Us</span>
  </div>
  <div class="abs foot-nav" style="left:0;width:1200px;top:150px">
    <span>Privacy Policy</span><span class="sep">/</span><span>Terms of Use</span>
  </div>
  <div class="abs" style="left:529px;top:188px;display:flex;gap:6px">
    <div class="social first"></div><div class="social"></div><div class="social"></div><div class="social"></div>
  </div>
  <div class="abs" style="left:111px;top:238px;width:978px;height:1px;background:#333"></div>
  <div class="abs" style="left:0;width:1200px;top:264px;text-align:center;font-size:12px;font-style:italic">&copy; 2022 <b>VELTA Finance</b> / All Rights Reserved</div>
</footer>

</body>
</html>
```